Veteran Reserved Parking Sign 12x18

Brave Hearts Kinship Network is looking to have a new Veteran Reserved Parking Sign designed. Included in the files are our current logo, the rectangle with the name on it. Also included is our Alt Square version that we will often use. There are several other signs that we kind of like as examples, not not asking for exactly like those, we want you to be creative and show us some new ideas. These are full sized parking signs, 12" wide X 18" height.

Target Market(s)

Veterans and Military Friendly Americans

Industry/Entity Type

Veteran Nonprofit

Font styles to use
Other font styles liked:
• Our logo uses the Franklin Heavy Gothic Font but you are not required to use that font in design.

Requirements
Must have
• Our logo needs to be on there and well as BHKN.ORG
Should not have
• CAN NOT Mention Steadfast Soldier Alliance or have black silhouettes similar to their logo. BHKN is NOT the same nonprofit.

```html
<!DOCTYPE html>
<html lang="en">
<head>
<meta charset="utf-8">
<title>Reserved Veteran Parking Sign</title>
<link rel="stylesheet" href="https://fonts.googleapis.com/css2?family=Saira+Condensed:wght@500;600;800&display=swap">
<style>
  :root {
    --flag-red: #b5003f;
    --flag-blue: #03197c;
    --flag-white: #ffffff;
    --page-bg: #ffffff;
  }
  html, body {
    margin: 0;
    padding: 0;
    width: 1200px;
    height: 1000px;
    overflow: hidden;
    background: var(--page-bg);
  }
  .parking-sign {
    display: block;
    width: 1200px;
    height: 1000px;
  }
  .sign-text {
    font-family: "Saira Condensed", sans-serif;
    fill: var(--flag-white);
    text-anchor: middle;
  }
  .headline { font-weight: 800; font-size: 114px; }
  .thanks-line { font-weight: 600; font-size: 38px; }
  .brand-name { font-weight: 800; font-size: 64px; }
  .brand-full-name { font-weight: 800; font-size: 17px; }
  .web-address { font-weight: 600; font-size: 33px; }
  .stripe-red { fill: var(--flag-red); }
  .stripe-white { fill: var(--flag-white); }
  .panel-border { fill: var(--flag-white); }
  .panel-field { fill: var(--flag-blue); }
  .star { fill: var(--flag-white); }
  .brand-mark { fill: var(--flag-white); }
</style>
</head>
<body>
<svg class="parking-sign" viewBox="0 0 1200 1000" xmlns="http://www.w3.org/2000/svg" aria-label="Reserved Veteran Parking sign">
  <defs>
    <clipPath id="sign-shape">
      <rect x="334" y="100" width="533" height="800" rx="67" ry="67"/>
    </clipPath>
  </defs>

  <!-- Striped background -->
  <g class="stripes" clip-path="url(#sign-shape)">
    <rect class="stripe-red" x="334" y="100" width="533" height="800"/>
    <rect class="stripe-white" x="411" y="100" width="75" height="800"/>
    <rect class="stripe-white" x="564" y="100" width="73" height="800"/>
    <rect class="stripe-white" x="714" y="100" width="75" height="800"/>
  </g>

  <!-- Central panel -->
  <path class="panel-border" d="M358 245 A242.5 111 0 0 1 843 245 L843 755 A242.5 111 0 0 1 358 755 Z"/>
  <path class="panel-field" d="M367 246 A233.5 104 0 0 1 834 246 L834 754 A233.5 104 0 0 1 367 754 Z"/>

  <!-- Headline -->
  <text class="sign-text headline" x="600" y="327" textLength="412" lengthAdjust="spacingAndGlyphs">RESERVED</text>
  <text class="sign-text headline" x="598" y="431" textLength="365" lengthAdjust="spacingAndGlyphs">VETERAN</text>
  <text class="sign-text headline" x="601" y="537" textLength="350" lengthAdjust="spacingAndGlyphs">PARKING</text>

  <!-- Thank-you message -->
  <text class="sign-text thanks-line" x="600" y="600" textLength="310" lengthAdjust="spacingAndGlyphs">THANK YOU FOR YOUR</text>
  <text class="sign-text thanks-line" x="601" y="637" textLength="296" lengthAdjust="spacingAndGlyphs">SERVICE &amp; SACRIFICE</text>

  <polygon class="star" transform="translate(408 608) scale(24)"
    points="0,-1 0.2245,-0.309 0.951,-0.309 0.363,0.118 0.588,0.809 0,0.382 -0.588,0.809 -0.363,0.118 -0.951,-0.309 -0.2245,-0.309"/>
  <polygon class="star" transform="translate(792 608) scale(24)"
    points="0,-1 0.2245,-0.309 0.951,-0.309 0.363,0.118 0.588,0.809 0,0.382 -0.588,0.809 -0.363,0.118 -0.951,-0.309 -0.2245,-0.309"/>

  <!-- Organisation name -->
  <g class="brand-lockup">
    <rect class="brand-mark" x="440" y="682" width="52" height="52"/>
    <text class="sign-text brand-name" x="630" y="731" textLength="240" lengthAdjust="spacingAndGlyphs">BHKN</text>
    <text class="sign-text brand-full-name" x="600" y="760" textLength="330" lengthAdjust="spacingAndGlyphs">Brave Hearts Kinship Network</text>
  </g>

  <!-- Web address -->
  <text class="sign-text web-address" x="600" y="800" textLength="118" lengthAdjust="spacingAndGlyphs">BHKN.ORG</text>
</svg>
</body>
</html>
```